Create a promo image to demo to a restaurant the increase in $ they can achieve by using Vesper

Create a promotional image to demonstrate to a restaurant the increase in revenue they can achieve by using Vesper.

We have constructed the attached example of what we are looking for, open to alternatives however the main message is you will make more money from a Vesper event than from your own restaurant for the same guests

We would like the restaurant image to look like the restaurant environment (show other tables in the background) and the same for the Customer dining room (plush private secure)

Please Vesper branding where it fits best

Target Market(s)

Restaurants to signup

Industry/Entity Type

Restaurants and Catering

Requirements
Must have
• Simplicity and obviousness

```html
<!DOCTYPE html>
<html lang="en">
<head>
<meta charset="utf-8">
<title>Why Vesper – Revenue Promo</title>
<link href="https://fonts.googleapis.com/css2?family=Poppins:wght@400;500;600;700;800&display=swap" rel="stylesheet">
<style>
:root{
  --purple:#7a1a7c;
  --yellow:#ffc400;
  --ink:#1c1c1c;
  --band:#232323;
  --light:#ececec;
  --stage:#e9e9e9;
  --white:#ffffff;
}
*{margin:0;padding:0;box-sizing:border-box}
html,body{width:1200px;height:995px;overflow:hidden;background:var(--stage);font-family:'Poppins',sans-serif;color:var(--ink)}
.card{position:absolute;left:75px;top:6px;width:1050px;height:983px;background:var(--white);overflow:hidden}
.abs{position:absolute}
.brand{left:60px;top:40px;width:150px;text-align:center}
.brand-dot{width:56px;height:56px;border-radius:50%;background:var(--purple);margin:0 auto 14px}
.brand-name{font-weight:600;color:var(--purple);font-size:17px;letter-spacing:5px;line-height:1.35}
.why{left:282px;top:40px;width:280px;font-weight:800;color:var(--purple);font-size:63px;line-height:.98;letter-spacing:-1px}
.headline{left:578px;top:38px;font-weight:800;font-size:44px;line-height:.95;text-transform:uppercase}
.art{border-radius:18px}
.art-venue{left:75px;top:272px;width:400px;height:225px;background:linear-gradient(180deg,#f3ece4,#e9d9c8)}
.art-home{left:585px;top:196px;width:390px;height:305px;background:linear-gradient(180deg,#f6efe6 0%,#e8c2a4 55%,#8a3322 100%)}
.bubble{display:flex;align-items:center;justify-content:center;text-align:center;font-weight:700;font-size:13px;line-height:1.05;border-radius:50%}
.bubble.purple{background:var(--purple);color:var(--white)}
.bubble.yellow{background:var(--yellow);color:var(--ink)}
.mode-title{width:320px;text-align:center;font-weight:700;font-size:31px;line-height:1}
.mode-sub{width:320px;text-align:center;font-weight:700;font-size:21px;color:var(--purple)}
.price{height:38px;border-radius:19px;background:var(--yellow);font-weight:700;font-size:32px;line-height:38px;text-align:center}
.price sup{font-size:17px;vertical-align:12px}
.note{width:380px;text-align:center;font-size:15.5px;line-height:1.25}
.band-dark{left:0;top:679px;width:1050px;height:40px;background:var(--band);color:var(--white);font-weight:700;font-size:28px;letter-spacing:5.3px;text-align:center;line-height:40px}
.band-yellow{left:0;top:719px;width:1050px;height:81px;background:var(--yellow)}
.benefit-title{font-weight:800;font-size:34px;color:var(--purple);line-height:1}
.benefit-text{font-size:19px;line-height:1.2}
.tagline{left:0;top:800px;width:377px;height:85px;background:var(--purple);color:var(--white);font-size:22px;line-height:1.25;padding:13px 0 0 52px}
.extras{left:377px;top:800px;width:673px;height:85px;background:var(--light)}
.extra-label{top:27px;font-weight:700;font-size:24px;letter-spacing:.5px}
.book{left:50px;top:910px;font-weight:700;font-size:24px}
.site{left:528px;top:905px;width:485px;height:42px;border-radius:21px;background:var(--band);color:var(--white);font-weight:700;font-size:24px;letter-spacing:6.5px;text-align:center;line-height:42px}
</style>
</head>
<body>
<div class="card">
  <div class="abs brand"><div class="brand-dot"></div><div class="brand-name">VESPER<br>DINING</div></div>
  <div class="abs why">WHY<br>VESPER?</div>
  <div class="abs headline">Triple your<br>revenue in<br>your downtime</div>

  <div class="abs art art-venue" role="img" aria-label="Illustration of a family sharing a meal at a restaurant table"></div>
  <div class="abs bubble purple" style="left:92px;top:213px;width:110px;height:80px">No<br>Canapes</div>
  <div class="abs bubble purple" style="left:335px;top:213px;width:110px;height:80px">Minimal<br>Cocktails</div>
  <div class="abs bubble purple" style="left:45px;top:475px;width:110px;height:80px">Minimal<br>Extras</div>
  <div class="abs bubble purple" style="left:375px;top:470px;width:110px;height:80px">Random<br>Ordering</div>

  <div class="abs mode-title" style="left:109px;top:508px">IN-VENUE</div>
  <div class="abs mode-sub" style="left:109px;top:538px">Business as usual</div>
  <div class="abs price" style="left:205px;top:575px;width:130px"><sup>$</sup>600</div>
  <div class="abs note" style="left:79px;top:621px">Staff costs in your menu pricing Inconsistent ordering No Guarantee of Spend</div>

  <svg class="abs" style="left:430px;top:560px" width="240" height="100" viewBox="0 0 240 100" aria-hidden="true">
    <path d="M10 20 L85 88 L210 25" fill="none" stroke="var(--purple)" stroke-width="7" stroke-linejoin="miter"/>
    <path d="M232 10 L196 12 L214 44 Z" fill="var(--purple)"/>
  </svg>

  <div class="abs art art-home" role="img" aria-label="Illustration of a large family dinner party in a home dining room"></div>
  <div class="abs bubble yellow" style="left:595px;top:193px;width:108px;height:78px">Canapes<br>for Everyone</div>
  <div class="abs bubble yellow" style="left:838px;top:200px;width:108px;height:78px">Cocktails for<br>Everyone</div>
  <div class="abs bubble yellow" style="left:590px;top:478px;width:110px;height:80px">Everyone has<br>everything</div>
  <div class="abs bubble yellow" style="left:888px;top:472px;width:112px;height:80px">3 courses for<br>Everyone</div>

  <div class="abs mode-title" style="left:642px;top:508px">IN-HOME</div>
  <div class="abs mode-sub" style="left:642px;top:538px">Create Experiences</div>
  <div class="abs price" style="left:735px;top:575px;width:130px"><sup>$</sup>1900</div>
  <div class="abs note" style="left:612px;top:621px">3X Plus Income Recession Proof Clients Immediate Positive Cashflow</div>

  <div class="abs band-dark">DINE AT YOUR FAVOURITE RESTAURANT AT HOME</div>
  <div class="abs band-yellow">
    <svg class="abs" style="left:90px;top:12px" width="46" height="56" viewBox="0 0 46 56" aria-hidden="true">
      <path d="M12 34 L4 52 L13 48 L17 55 L23 40 Z M34 34 L42 52 L33 48 L29 55 L23 40 Z" fill="var(--ink)"/>
      <circle cx="23" cy="22" r="21" fill="var(--ink)"/>
      <path d="M23 9 L27 18 L36 19 L29 25 L31 34 L23 29 L15 34 L17 25 L10 19 L19 18 Z" fill="var(--yellow)"/>
    </svg>
    <div class="abs benefit-title" style="left:155px;top:12px">Achieve 3+ times</div>
    <div class="abs benefit-text" style="left:157px;top:48px">the spend for the same number</div>
    <svg class="abs" style="left:512px;top:9px" width="66" height="64" viewBox="0 0 66 64" aria-hidden="true">
      <path d="M14 4 H34 L28 16 H20 Z" fill="var(--ink)"/>
      <path d="M20 18 H28 C46 28 48 60 24 60 C0 60 2 28 20 18 Z" fill="var(--ink)"/>
      <text x="24" y="50" text-anchor="middle" font-family="Poppins,sans-serif" font-weight="800" font-size="22" fill="var(--yellow)">$</text>
      <rect x="44" y="30" width="20" height="6" rx="3" fill="var(--ink)"/>
      <rect x="44" y="40" width="20" height="6" rx="3" fill="var(--ink)"/>
      <rect x="44" y="50" width="20" height="6" rx="3" fill="var(--ink)"/>
    </svg>
    <div class="abs benefit-title" style="left:595px;top:12px">Cover your staff cost</div>
    <div class="abs benefit-text" style="left:595px;top:48px">over and above your menu spend</div>
  </div>

  <div class="abs tagline">Vespers are an occasion and everyone has everything</div>
  <div class="abs extras">
    <svg class="abs" style="left:30px;top:20px" width="46" height="48" viewBox="0 0 46 48" aria-hidden="true">
      <path d="M2 6 H36 L19 26 Z" fill="var(--purple)"/>
      <rect x="17" y="25" width="4" height="16" fill="var(--purple)"/>
      <rect x="9" y="40" width="20" height="4" rx="2" fill="var(--purple)"/>
      <circle cx="37" cy="9" r="7" fill="var(--yellow)"/>
    </svg>
    <div class="abs extra-label" style="left:93px">COCKTAILS</div>
    <svg class="abs" style="left:263px;top:26px" width="48" height="36" viewBox="0 0 48 36" aria-hidden="true">
      <path d="M4 26 A20 20 0 0 1 44 26 Z" fill="var(--yellow)"/>
      <circle cx="24" cy="5" r="3" fill="var(--yellow)"/>
      <rect x="0" y="28" width="48" height="6" rx="3" fill="var(--purple)"/>
    </svg>
    <div class="abs extra-label" style="left:325px">SIDES</div>
    <svg class="abs" style="left:428px;top:20px" width="46" height="46" viewBox="0 0 46 46" aria-hidden="true">
      <line x1="4" y1="42" x2="42" y2="4" stroke="var(--purple)" stroke-width="3"/>
      <rect x="10" y="22" width="14" height="14" rx="3" transform="rotate(45 17 29)" fill="var(--yellow)"/>
      <rect x="22" y="10" width="14" height="14" rx="3" transform="rotate(45 29 17)" fill="var(--yellow)"/>
    </svg>
    <div class="abs extra-label" style="left:488px">CANAPES</div>
  </div>

  <div class="abs book">For your intimate event, book us at</div>
  <div class="abs site">www.vesperdining.com</div>
</div>
</body>
</html>
```